The homepage of a website

This is a simple project that should take from you a few minutes as what is needed is the design of the homepage only, the details are in the attached zip file

Please note that KLVTA board required a special tailored design where they got some parts from the different posted designs, if you are interested please follow the instructions in the below URL and submit your new updated designs as per the instructions (P.S. I will mark the project as guaranteed as an assurance to all of you)

http://qorvinworks.example/Projects/KLVTA/Design.jpg
Updates

Please note that KLVTA board required a special tailored design where they got some parts from the different posted designs, if you are interested please follow the instructions in the below URL and submit your new updated designs as per the instructions (P.S. I will mark the project as guaranteed as an assurance to all of you) http://qorvinworks.example/Projects/KLVTA/Design.jpg

```html
<!DOCTYPE html>
<html lang="en">
<head>
<meta charset="utf-8">
<title>KLVTA — Home</title>
<link href="https://fonts.googleapis.com/css2?family=Montserrat:wght@400;500;600&family=Ubuntu:wght@400;500&display=swap" rel="stylesheet">
<style>
:root{
  --navy:#1b4a7e;
  --nav:#143e6b;
  --blue:#1a6fc0;
  --link:#2f7fd0;
  --sky:#22b8ee;
  --orange:#e8582a;
  --green:#7bbf3a;
  --text:#555;
  --line:#d5dbe2;
  --footer:#1d3f68;
  --footer-box:#17355a;
}
*{margin:0;padding:0;box-sizing:border-box}
html,body{width:800px;height:1200px;overflow:hidden}
body{font-family:"Montserrat",sans-serif;color:var(--text);
  background:radial-gradient(ellipse at 50% 45%,#38c9f5 0%,#1aa2e6 45%,#0b6cc0 100%);position:relative}
.topbar{position:absolute;left:0;top:0;width:800px;height:21px;background:linear-gradient(#1d5d98,#164d85);}
.topbar a{position:absolute;top:6px;font-size:6.5px;color:#cfe2f5;text-decoration:none}
.lang{position:absolute;left:630px;top:3px;width:42px;height:14px;background:var(--orange);color:#fff;font-size:6.5px;font-weight:600;padding:3px 0 0 8px}
.lang::after{content:"▾";position:absolute;right:5px;top:3px;font-size:6px}
.page{position:absolute;left:120px;top:21px;width:560px;height:1045px;background:#fff}
.abs{position:absolute}
.logo{left:8px;top:5px;width:140px;height:57px;background:linear-gradient(90deg,#fff,#c9d7f0);display:flex;align-items:center;padding-left:12px;gap:6px}
.logo .dot{width:14px;height:14px;border-radius:50%;background:var(--navy)}
.logo span{font-size:15px;font-weight:600;color:var(--navy)}
.banner{left:148px;top:5px;width:404px;height:57px;background:linear-gradient(90deg,#1f5fd0,#1249b8);display:flex;align-items:center;padding-left:60px;color:#fff;font-size:10px;line-height:1.35}
.nav{left:8px;top:69px;width:544px;height:24px;background:var(--nav);display:flex;align-items:center}
.nav a{color:#fff;font-size:6.5px;text-decoration:none;padding:0 11px;height:24px;line-height:24px;border-right:1px solid #2a5789}
.nav a:first-child{padding-left:15px}
.nav .search{margin-left:auto;margin-right:6px;width:88px;height:13px;background:#fff;border-radius:2px;font-size:5.5px;color:#aaa;padding:3px 6px}
.hero{left:8px;top:93px;width:544px;height:214px;background:linear-gradient(110deg,#1d4f86 0%,#3d6f9e 45%,#b98a6c 70%,#d6c1b4 100%)}
.hero h1{position:absolute;left:9px;top:64px;font-family:"Ubuntu",sans-serif;font-weight:400;color:#fff;font-size:17px;line-height:21px}
.hero h1 em{font-style:normal;color:#35aef5;font-size:21px}
.sec-title{font-size:10px;color:var(--navy);display:flex;align-items:center;gap:4px;font-weight:500}
.sec-title svg{width:13px;height:13px}
p.small{font-size:6.3px;line-height:11px;color:var(--text)}
.field{position:absolute;left:8px;font-size:6.5px;color:var(--link)}
.input{position:absolute;left:52px;width:154px;height:13px;border:1px solid #ccd4dc;border-radius:2px}
.btn{position:absolute;background:var(--orange);color:#fff;font-size:5.8px;font-weight:600;text-align:center;border-radius:2px}
.poster{left:310px;top:326px;width:94px;height:127px;border:3px solid #e3e3e3;background:linear-gradient(#f5f3ee,#e9dfe8 55%,#5a8ac0 85%,#c7a060)}
.calendar{left:420px;top:325px;width:130px;height:127px;border-radius:8px;background:linear-gradient(#f3f3f3,#d9d9d9);box-shadow:0 2px 4px rgba(0,0,0,.25)}
.divider{position:absolute;left:8px;width:544px;height:1px;background:var(--line)}
.feature{position:absolute;top:491px;width:150px;text-align:center}
.feature .ring{width:70px;height:70px;border-radius:50%;border:2px solid var(--navy);margin:0 auto;display:flex;align-items:center;justify-content:center}
.feature .ring.solid{background:var(--navy)}
.feature h3{font-size:9.5px;font-weight:500;color:var(--blue);margin-top:14px}
.feature p{margin-top:6px;font-size:6.2px;line-height:13px}
.strip{left:8px;top:679px;width:544px;height:108px;background:#f6f7f9;border:1px solid #eceef1}
.thumb{position:absolute;top:9px;width:96px;height:88px}
.arrow{position:absolute;top:48px;font-size:9px;color:#b9c0c8}
.col-title{font-size:10px;color:var(--blue);display:flex;align-items:center;gap:5px;font-weight:500}
.col-title svg{width:13px;height:13px}
.under{position:absolute;height:1px;background:var(--line)}
.item{position:absolute;width:170px;height:54px}
.item .pic{position:absolute;left:0;top:0;width:56px;height:54px;background:linear-gradient(135deg,#8e9a7c,#cfa27a 60%,#4a6a8a)}
.item h4{position:absolute;left:61px;top:1px;font-size:8px;font-weight:400;color:var(--link)}
.item .date{position:absolute;left:61px;top:13px;font-size:6px;color:var(--orange)}
.item p{position:absolute;left:61px;top:23px;font-size:6px;line-height:9.7px;width:110px}
.partners-title{font-size:10px;color:var(--link)}
.footer{position:absolute;left:0;top:1045px;width:560px;height:134px;background:var(--footer)}
.flinks{position:absolute;left:8px;top:18px;width:195px;height:106px;background:var(--footer-box);display:grid;grid-template-columns:98px 97px;grid-auto-rows:16.2px;padding:8px 0 0 10px}
.flinks a{color:#fff;font-size:6.3px;text-decoration:none}
.flinks a::before{content:"▸ ";font-size:5px;color:#9fb8d4}
.footer h5{position:absolute;font-size:10px;font-weight:400;color:#fff}
.footer p{position:absolute;font-size:6.3px;line-height:12px;color:#e2ebf5}
.nl-input{position:absolute;left:258px;top:73px;width:126px;height:14px;background:#fff;border-radius:2px}
.sub{position:absolute;left:258px;top:97px;width:50px;height:14px;background:var(--green);color:#fff;font-size:6.3px;text-align:center;line-height:14px;border-radius:2px}
.social{position:absolute;top:35px;width:15px;height:15px;border-radius:50%;background:#fff}
</style>
</head>
<body>
<div class="topbar">
  <a style="left:558px">Login</a><a style="left:592px">Register</a>
  <div class="lang">ENG</div>
</div>

<div class="page">
  <div class="abs logo"><div class="dot"></div><span>KLVTA</span></div>
  <div class="abs banner">The Kelvara Society of Plastic<br>&amp; Reconstructive Surgeons</div>

  <nav class="abs nav">
    <a>Home</a><a>Board</a><a>History</a><a>Members</a><a>Activities</a><a>Laws</a><a>Journal</a><a>Downloads</a><a>Links</a><a>Contact</a>
    <div class="search">Search ...</div>
  </nav>

  <div class="abs hero" role="img" aria-label="Surgeons' gloved hands operating with surgical instruments">
    <h1>The Kelvara Society<br>of Plastic <em>&amp; revonstructive</em><br><em>Surgeons</em></h1>
  </div>

  <!-- member search -->
  <div class="abs sec-title" style="left:5px;top:330px">
    <svg viewBox="0 0 14 14"><circle cx="6" cy="6" r="4.2" fill="none" stroke="#1b4a7e" stroke-width="1.8"/><path d="M9 9l4 4" stroke="#1b4a7e" stroke-width="2"/></svg>
    Search KLVTA Members
  </div>
  <p class="abs small" style="left:8px;top:345px;width:296px">Lorem ipsum dolor sit amet, consectetur adipiscing elit, sed do eiusmod tempor incid idunt ut labore et dolore magna aliqua.</p>
  <div class="field" style="top:373px">Name :</div><div class="input" style="top:370px"></div>
  <div class="field" style="top:397px">Address :</div><div class="input" style="top:394px"></div>
  <div class="field" style="top:421px">Speciality :</div><div class="input" style="top:418px"></div>
  <div class="btn" style="left:8px;top:441px;width:46px;height:16px;line-height:16px">SEARCH</div>

  <div class="abs poster" role="img" aria-label="Annual international conference poster"></div>
  <div class="abs calendar" role="img" aria-label="Page-curl calendar for January 2015 with the 4th circled"></div>

  <div class="divider" style="top:467px"></div>

  <div class="feature" style="left:12px">
    <div class="ring solid"><svg width="34" height="30" viewBox="0 0 34 30"><path d="M17 4L2 11l15 7 15-7z" fill="#fff"/><path d="M8 14v7c3 3 15 3 18 0v-7l-9 4z" fill="#fff"/></svg></div>
    <h3>Universities</h3>
    <p>Lorem ipsum dolor sit amet, consectetur<br>adipiscing elit, sed do eiusmod temp<br>or incid idunt ut labore et dolore</p>
  </div>
  <div class="feature" style="left:205px">
    <div class="ring"><svg width="36" height="28" viewBox="0 0 36 28"><circle cx="11" cy="8" r="4" fill="#1b4a7e"/><circle cx="25" cy="11" r="3.5" fill="#1b4a7e"/><path d="M4 22c0-6 3-9 7-9s7 3 7 9zM19 22c0-5 2-7 6-7s6 2 6 7z" fill="#1b4a7e"/><rect x="2" y="23" width="32" height="2" fill="#1b4a7e"/></svg></div>
    <h3>E-learning</h3>
    <p>Lorem ipsum dolor sit amet, consectetur<br>adipiscing elit, sed do eiusmod temp<br>or incid idunt ut labore et dolore</p>
  </div>
  <div class="feature" style="left:397px">
    <div class="ring"><svg width="32" height="30" viewBox="0 0 32 30"><rect x="10" y="3" width="19" height="20" fill="none" stroke="#1b4a7e" stroke-width="2"/><circle cx="9" cy="12" r="3.5" fill="#1b4a7e"/><path d="M2 27c0-7 3-10 7-10l9-6 1 2-7 7v7z" fill="#1b4a7e"/></svg></div>
    <h3>Patients education</h3>
    <p>Lorem ipsum dolor sit amet, consectetur<br>adipiscing elit, sed do eiusmod temp<br>or incid idunt ut labore et dolore</p>
  </div>

  <div class="divider" style="top:645px"></div>

  <div class="abs sec-title" style="left:6px;top:661px">
    <svg viewBox="0 0 14 14"><rect x="1" y="3" width="11" height="9" fill="none" stroke="#1b4a7e" stroke-width="1.4"/><path d="M3 10l3-3 2 2 2-2 2 3z" fill="#1b4a7e"/></svg>
    Our Gallery
  </div>
  <div class="abs strip">
    <span class="arrow" style="left:6px">‹</span>
    <div class="thumb" role="img" aria-label="Surgical team in an operating room" style="left:20px;background:linear-gradient(135deg,#1f7d7a,#5aa7a0 50%,#2b5a66)"></div>
    <div class="thumb" role="img" aria-label="Doctor's gloved hands examining a patient" style="left:122px;background:linear-gradient(135deg,#c9d6e2,#7fb2e0 55%,#e8cfc0)"></div>
    <div class="thumb" role="img" aria-label="Cosmetic injection treatment" style="left:225px;background:linear-gradient(135deg,#c07a5c,#e6c4ae 55%,#8a4a3a)"></div>
    <div class="thumb" role="img" aria-label="Facial skin treatment" style="left:327px;background:linear-gradient(135deg,#e9ddd6,#d8c3b8 55%,#f2ece8)"></div>
    <div class="thumb" role="img" aria-label="Before and after facial comparison" style="left:430px;background:linear-gradient(135deg,#d4b6a4,#a47c68 55%,#e8d8cc)"></div>
    <span class="arrow" style="left:532px">›</span>
  </div>

  <!-- news / events / journal -->
  <div class="abs col-title" style="left:8px;top:806px"><svg viewBox="0 0 14 14"><path d="M1 9l8-6 4 3-8 6z" fill="none" stroke="#1b4a7e" stroke-width="1.3"/><path d="M3 10l7-5" stroke="#1b4a7e"/></svg>News</div>
  <div class="under" style="left:8px;top:819px;width:170px"></div>
  <div class="item" style="left:8px;top:829px"><div class="pic" role="img" aria-label="Surgery in progress"></div><h4>Ipsum dolar sit</h4><div class="date">12 jan 2015</div><p>Lorem ipsum dolor sit amet, adipiscing elit, sed do eiusmo or incid idunt ut</p></div>
  <div class="item" style="left:8px;top:900px"><div class="pic" role="img" aria-label="Surgery in progress"></div><h4>Ipsum dolar sit</h4><div class="date">12 jan 2015</div><p>Lorem ipsum dolor sit amet, adipiscing elit, sed do eiusmo or incid idunt ut</p></div>

  <div class="abs col-title" style="left:194px;top:806px"><svg viewBox="0 0 14 14"><rect x="1" y="2" width="12" height="11" fill="none" stroke="#1b4a7e" stroke-width="1.3"/><rect x="1" y="2" width="12" height="3" fill="#1b4a7e"/><path d="M4 7h2v2H4zM8 7h2v2H8zM4 10h2v2H4z" fill="#1b4a7e"/></svg>Up coming Events</div>
  <div class="under" style="left:192px;top:819px;width:172px"></div>
  <div class="item" style="left:192px;top:829px"><div class="pic" role="img" aria-label="Surgery in progress"></div><h4>Ipsum dolar sit</h4><div class="date">12 jan 2015</div><p>Lorem ipsum dolor sit amet, adipiscing elit, sed do eiusmo or incid idunt ut</p></div>
  <div class="item" style="left:192px;top:900px"><div class="pic" role="img" aria-label="Surgery in progress"></div><h4>Ipsum dolar sit</h4><div class="date">12 jan 2015</div><p>Lorem ipsum dolor sit amet, adipiscing elit, sed do eiusmo or incid idunt ut</p></div>

  <div class="abs col-title" style="left:382px;top:806px"><svg viewBox="0 0 14 14"><rect x="2" y="1" width="9" height="12" fill="#1b4a7e"/><circle cx="10" cy="10" r="2.5" fill="#fff" stroke="#1b4a7e"/></svg>KLVTA Journal</div>
  <div class="under" style="left:382px;top:819px;width:170px"></div>
  <p class="abs small" style="left:382px;top:825px;width:168px;line-height:13px">Lorem ipsum dolor sit amet, consectetur adipiscing elit, sed do eiusmod tempor incid idunt ut labore et dolore magna aliqua. Ut enim ad minim veniam,</p>
  <p class="abs small" style="left:382px;top:890px;width:168px;line-height:13px">quis nostrud exercita tion ullamco laboris met, consectetur adipiscing elit, sed do eiusmod tempor incid idunt ut labore.</p>
  <div class="btn" style="left:382px;top:936px;width:45px;height:16px;line-height:16px">SEARCH</div>

  <div class="divider" style="top:973px"></div>

  <div class="abs partners-title" style="left:8px;top:1001px">Our Partners</div>
  <svg class="abs" style="left:96px;top:984px" width="450" height="50" viewBox="0 0 450 50">
    <circle cx="23" cy="24" r="20" fill="#d8dde8"/>
    <circle cx="104" cy="23" r="17" fill="#c4d6e4"/>
    <circle cx="198" cy="17" r="14" fill="none" stroke="#1a6fa0" stroke-width="2"/>
    <circle cx="275" cy="24" r="11" fill="#c8202e"/><rect x="292" y="17" width="63" height="14" fill="#c9b79a"/>
    <circle cx="381" cy="24" r="8" fill="#9a9a9a"/><rect x="394" y="16" width="56" height="16" fill="#b5b5b5"/>
  </svg>

  <footer class="footer">
    <div class="flinks">
      <a>Home</a><a>Journal</a><a>Board</a><a>Downloads</a><a>History</a><a>Links</a><a>Members</a><a>Contact</a><a>Activities</a><span></span><a>Laws</a>
    </div>
    <h5 style="left:258px;top:20px">Newsletter signup</h5>
    <p style="left:258px;top:41px;width:130px">Enter your email and subscribe our bio monthly newsletter</p>
    <div class="nl-input"></div>
    <div class="sub">Subscribe</div>
    <h5 style="left:442px;top:20px">Follow us on</h5>
    <div class="social" style="left:443px"></div><div class="social" style="left:465px"></div><div class="social" style="left:487px"></div>
    <p style="left:442px;top:59px">Terms &amp; Conditions<br>Privacy Policy</p>
    <p style="left:442px;top:91px">Copyrights © KLVTA 2015<br>by KLVTA.com All right reservds.</p>
  </footer>
</div>
</body>
</html>
```